Meadow Voyages Web Page Redesign

IF YOu ARE IN INDIA - PLEASE PLEASE PLEASE - make sure you are working off of MEADOWVOYAGES.COM - Not another site. Look at the URL above when you see the site!

Our website http://www.meadowvoyages.com is driven by a backend database providing content. We are interested in redesigning the website layout to make it responsive and also to make it more interesting, catchy and call to action oriented. Right now it seems not to be able to deliver the message and a little crowded. The main template pages to be addressed are index.aspx, default.aspx, TourList1.aspx, and the actual tour detail page.

There needs to be tight integration / prominent visibility for Social Media.

Focus needs to be on design that would reduce the bounce rate and be SEO friendly.

You will be responsible for layout and delivering the front end css / layout / slices to integrate with the back end.
Updates

If you are based in India, you are probably going to be redirected to another site. Please make sure you are working off of MEADOWVOYAGES.COM

Target Market(s)

It is a B2C site - travelers who are interested in traveling to India, Europe and South Africa.

Industry/Entity Type

Media

Font styles to use
Sans Serif

Requirements
Must have
• ONE VERY IMPORTANT POINT : We have a number of photographs that we would love to put online. Unfortunately our current design requires us to resize / crop the photographs which make them lose the impact. We would prefer a design where the images could be used as-is.

Tight integration with Social Media is there in our engine so it should be visible on the website.

Responsive.
Nice to have
• Try using the same color scheme but we are open for changes in the same tone..

```html
<!DOCTYPE html>
<html lang="en">
<head>
<meta charset="utf-8">
<title>Meadow Voyages</title>
<link href="https://fonts.googleapis.com/css2?family=Cabin:wght@400;500;600&display=swap" rel="stylesheet">
<style>
:root{
  --red:#d21f2b;
  --orange:#dc7104;
  --orange-text:#e07a10;
  --ink:#222;
  --white:#fff;
  --dark:#2b2b2b;
  --grey:#555;
  --photo-a:#b89a5c;
  --photo-b:#8a6a3a;
  --photo-c:#c7b27a;
}
*{box-sizing:border-box;margin:0;padding:0}
html,body{width:1085px;height:1200px;overflow:hidden}
body{position:relative;font-family:"Cabin",sans-serif;color:var(--ink);background:var(--white)}
.abs{position:absolute}
.hero-photo{left:0;top:0;width:1085px;height:373px;
  background:radial-gradient(ellipse at 45% 45%,var(--photo-c),var(--photo-a) 45%,var(--photo-b) 100%)}
.brand-card{left:162px;top:53px;width:169px;height:191px;background:var(--white)}
.brand-mark{left:0;top:0;width:169px;height:110px;display:flex;align-items:center;justify-content:center;gap:8px;color:var(--red);font-size:17px;font-weight:500}
.brand-mark .dot{width:14px;height:14px;border-radius:50%;background:var(--red)}
.brand-band{left:6px;top:110px;width:163px;height:43px;background:var(--red);color:var(--white);font-size:16px;display:flex;align-items:center;justify-content:center;white-space:nowrap}
.trip-select{left:6px;top:153px;width:163px;height:38px;padding:4px 12px}
.trip-select .label{color:var(--orange-text);font-size:12px}
.trip-select .value{font-size:9px;color:var(--grey)}
.trip-select svg{position:absolute;right:10px;top:22px}
.intro-panel{left:575px;top:50px;width:342px;height:224px;background:rgba(245,240,230,.88)}
.intro-panel .accent{left:0;top:0;width:53px;height:5px;background:var(--red)}
.social{right:14px;top:7px;display:flex;gap:9px;list-style:none}
.social li{color:var(--red);font-size:11px;font-weight:600;line-height:13px}
.intro-panel h2{left:25px;top:32px;font-size:14px;font-weight:600}
.intro-panel p{left:25px;top:57px;width:300px;font-size:14px;line-height:19px}
.intro-panel p b{float:right;font-weight:600}
.dots{left:27px;top:192px;display:flex;gap:5px}
.dots span{width:13px;height:13px;border-radius:50%;background:var(--white)}
.dots span.on{background:var(--orange)}
.btn-red{background:var(--red);color:var(--white);display:flex;align-items:center;justify-content:center;font-size:14px}
.all-trips{left:194px;top:192px;width:148px;height:32px}
.main-nav{left:166px;top:322px;width:751px;height:51px;background:var(--orange);display:flex;align-items:center;padding-left:10px}
.main-nav a{color:var(--white);text-decoration:none;font-size:15px;padding:0 6px;border-right:1px solid rgba(255,255,255,.5);line-height:28px}
.main-nav a:last-of-type{border-right:none}
.search{margin-left:10px;width:81px;height:22px;background:var(--white);border-radius:11px;font-size:10px;color:#999;padding:4px 10px;position:relative}
.search svg{position:absolute;right:8px;top:5px}
.section-title{font-size:17px;font-weight:400;color:var(--red)}
.section-title.orange{color:var(--orange-text)}
.underline{height:5px;width:137px}
.deal-photo{width:110px;height:79px}
.deal-text{width:238px;font-size:14px;line-height:14.5px}
.deal-text b{display:block;text-align:right;font-weight:400}
.testimonials{left:0;top:631px;width:1085px;height:351px;background:var(--orange)}
.quote-mark{left:166px;width:28px;height:7px;background:var(--white)}
.quote{left:234px;width:672px;color:var(--white);font-size:12.6px;line-height:14.5px}
.quote .who{margin-top:14px;font-size:12.6px}
.quote .trip{font-style:italic;font-size:11px}
.btn-white{background:var(--white);color:var(--orange-text);font-size:14px;display:flex;align-items:center;justify-content:center}
.foot-links{left:158px;top:1014px;font-size:12px;line-height:14.5px;list-style:none}
.listing-badge{left:314px;top:1008px;width:68px;height:88px;background:#e8dfc7;border:3px solid #c7a35a}
.offer-text{left:532px;top:1015px;font-size:13px;line-height:15px}
.email{left:462px;top:1056px;width:181px;height:36px;border:1px solid var(--red);border-radius:9px;font-size:13px;padding:9px 14px}
.send{left:659px;top:1057px;width:66px;height:34px;background:#444;color:var(--white);border-radius:9px;font-size:13px;display:flex;align-items:center;justify-content:center}
.foot-brand{left:763px;top:1012px;width:151px;height:78px;display:flex;align-items:center;justify-content:center;gap:8px;color:#888;font-size:16px;font-weight:500}
.foot-brand .dot{width:12px;height:12px;border-radius:50%;background:#888}
.legal{left:0;top:1123px;width:1085px;height:77px;background:var(--dark);color:var(--white);font-size:11px;padding:20px 0 0 158px;line-height:15px}
</style>
</head>
<body>
<div class="abs hero-photo" role="img" aria-label="Close-up photograph of a young cheetah on the savanna"></div>

<div class="abs brand-card">
  <div class="abs brand-mark"><span class="dot"></span>Meadow Voyages</div>
  <div class="abs brand-band">MEADOW VOYAGES</div>
  <div class="abs trip-select">
    <div class="label">SELECT A TRIP</div>
    <div class="value">INDIA, NEPAL...</div>
    <svg width="10" height="8" viewBox="0 0 10 8"><path d="M0 0h10L5 8z" fill="#d21f2b"/></svg>
  </div>
</div>

<div class="abs intro-panel">
  <div class="abs accent"></div>
  <ul class="abs social" aria-label="Follow us"><li>Chirply</li><li>Facenet</li><li>Pixlo</li></ul>
  <h2 class="abs">SOUTH AFRICA</h2>
  <p class="abs">We will help you find the perfect vacation in Africa to suit your needs, whether you prefer north, south, east, west, or somewhere in between. We offer exciting safari packages, private game lodge escapes, wine tasting experiences, unparalleled luxury rail journeys and more! <b>READ MORE</b></p>
  <div class="abs dots"><span class="on"></span><span></span><span></span><span></span><span></span></div>
  <div class="abs btn-red all-trips">SEE ALL OUR TRIPS</div>
</div>

<nav class="abs main-nav">
  <a>TOUR CALENDAR</a><a>JOB OPPORTUNITIES</a><a>CONTACT US</a><a>ABOUT US</a><a>BUY TRAVEL INSURANCE</a>
  <div class="search">search
    <svg width="11" height="11" viewBox="0 0 11 11"><circle cx="4.5" cy="4.5" r="3.5" fill="none" stroke="#dc7104" stroke-width="1.6"/><path d="M7 7l3 3" stroke="#dc7104" stroke-width="1.6"/></svg>
  </div>
</nav>

<h3 class="abs section-title" style="left:168px;top:406px">TRAVEL DEALS</h3>
<div class="abs underline" style="left:168px;top:433px;background:var(--red)"></div>
<svg class="abs" style="left:885px;top:403px" width="34" height="18" viewBox="0 0 34 18"><path d="M7 2L2 9l5 7M27 2l5 7-5 7" fill="none" stroke="#d21f2b" stroke-width="2"/></svg>

<div class="abs deal-photo" style="left:168px;top:456px;background:linear-gradient(160deg,#8fa3b8,#6a5a48)" role="img" aria-label="Photograph of a cathedral in Spain"></div>
<div class="abs deal-text" style="left:295px;top:454px">10% OFF special offer for our Senior Citizen Guests for all our guided bus tours in Spain<b>READ MORE</b></div>
<div class="abs deal-photo" style="left:551px;top:456px;background:linear-gradient(160deg,#b4502c,#6b2418)" role="img" aria-label="Photograph of a luxury train dining car"></div>
<div class="abs deal-text" style="left:678px;top:454px;width:241px">Take 10% Off Royal Rail Express - Rajasthan by Luxury Rail tour<b>READ MORE</b></div>

<div class="abs btn-red" style="left:448px;top:560px;width:183px;height:24px">VIEW ALL TRAVEL DEALS</div>

<h3 class="abs section-title orange" style="left:168px;top:598px">TESTIMONIALS</h3>
<div class="abs underline" style="left:168px;top:624px;background:var(--orange)"></div>

<section class="abs testimonials"></section>
<div class="abs quote-mark" style="top:656px"></div>
<div class="abs quote" style="top:654px">“From start to finish, the Royal Rail Express and Nepal exceeded my wildest expectations. Every possible need or want was anticipated and fulfilled. I could not ask for better service and am grateful for making it possible to visit India and Nepal, places where a solo traveler might encounter some difficulty. Sincere thanks to the entire staff!”
  <div class="who">Daniel - Prospect Park,United States of America</div>
  <div class="trip">Traveled in November, 2013 - Royal Rail Express and the Delights of Nepal</div>
</div>
<div class="abs quote-mark" style="top:759px"></div>
<div class="abs quote" style="top:756px">“A very memorable trip. We've travelled a lot, including a couple of luxury train trips, but this was the best.”
  <div class="who">Thomas - Worplesdon,United Kingdom of Great Britain &amp; N. Ireland</div>
  <div class="trip">Traveled in November, 2013 - A Week in Wonderland : Royal Rail Express</div>
</div>
<div class="abs quote-mark" style="top:830px"></div>
<div class="abs quote" style="top:827px">“A lot of places in just one week, we saved a lot of time while the train moved when we slept. The guides were excellent and the staff of the train very friendly and nice. We were treated like real majarahs!”
  <div class="who">Lucia - Lima,Peru</div>
  <div class="trip">Traveled in November, 2013 - Desert Crown Rail</div>
</div>
<div class="abs btn-white" style="left:450px;top:931px;width:183px;height:24px">VIEW ALL TESTIMONIALS</div>

<ul class="abs foot-links">
  <li>HOME</li><li>ABOUT US</li><li>CONTACT US</li><li>EMPLOYMENT</li><li>AGENTS AREA</li><li>SITE MAP</li>
</ul>
<div class="abs listing-badge"></div>
<svg class="abs" style="left:461px;top:1015px" width="43" height="27" viewBox="0 0 43 27"><rect width="43" height="27" fill="#d21f2b"/><path d="M1 1l20.5 15L42 1" fill="none" stroke="#fff" stroke-width="2"/></svg>
<div class="abs offer-text">INTERESTED IN KNOWING ABOUT<br>OUR SPECIAL OFFERS?</div>
<div class="abs email">email address</div>
<div class="abs send">SEND</div>
<div class="abs foot-brand"><span class="dot"></span>Meadow Voyages</div>

<footer class="abs legal">©2008-2014 MEADOW VOYAGES LTD, ALL RIGHTS RESERVED<br>CORPORATE OFFICE: 45 ELM ROW, FAIRVIEW, NJ, 08000 | PHONE: 555-010-1372 | FAX: 555-010-9772 | TOLL FREE: 1-800-555-0142 OR 1-800-555-0177</footer>
</body>
</html>
```